I need a great design for my Ebook because that will help spread the message

Hey there,

I wrote an eBook (THE MORNING LANTERN METHOD) about how confidence impacts one's life, why it’s important and how to get more of it and I need someone to design it nicely.

My target audience is made up of more women than men.

I have pictures for each one of the 7 steps in the book, but I am open to your suggestions.

I really like Optima as a font. I have a bit of gold in the text. I would be happy if you could keep it. You can format the text as you think best.

I'd love a modern design.

I added an old design of the ebook for you to see the way the pictures are used for each step because I want to keep that blend between the picture and the title of the step.
I like the idea of each step starting on a new page and the block footer - just not black.

I want the subtitle of each step to be a different font to the title.

Please ask any questions you have.

Thank you!

Target Market(s)

Men and women aged 25-45.

Industry/Entity Type

Life Coaching

Font styles to use
Sans Serif

Colors
ffffff

Requirements
Must have
• My brand colours only:
• navy #233264
• white
• light pink #fff3f1
• mustard yellow #ffc800.
Nice to have
• The pictures I uploaded for each step.
Should not have
• Should not have much black.

```html
<!DOCTYPE html>
<html lang="en">
<head>
<meta charset="utf-8">
<title>The Morning Lantern Method — eBook Cover</title>
<link rel="stylesheet" href="https://fonts.googleapis.com/css2?family=Marcellus&family=Josefin+Sans:wght@300;600&display=swap">
<style>
  :root {
    --navy: #233264;
    --blush: #fff3f1;
    --gold: #ffc800;
    --white: #ffffff;
  }
  * { margin: 0; padding: 0; box-sizing: border-box; }
  html, body { width: 800px; height: 1200px; overflow: hidden; background: var(--white); }
  .cover { position: relative; width: 800px; height: 1200px; background: var(--blush); }

  .step-strip { position: absolute; left: 0; top: 0; width: 400px; height: 1200px; display: flex; flex-direction: column; }
  .step-photo { width: 100%; flex: none; }
  .step-toys { height: 182px; background: linear-gradient(180deg, #f1e3c8 0%, #e8605a 45%, #f3c22b 75%, #cfe3ee 100%); }
  .step-tools { height: 162px; background: linear-gradient(135deg, #b9bcbd 0%, #8f9394 50%, #c6cacb 100%); }
  .step-sand { height: 172px; background: linear-gradient(180deg, #b3b2b0 0%, #9c9b99 100%); }
  .step-mic { height: 172px; background: linear-gradient(90deg, #5a4a3e 0%, #d9d6d2 40%, #7aa0c0 65%, #e9ecef 100%); }
  .step-thanks { height: 172px; background: linear-gradient(180deg, #ffffff 0%, #f4f0ea 35%, #d8743a 65%, #fafafa 100%); }
  .step-calm { height: 172px; background: linear-gradient(180deg, #e6f0f4 0%, #c9d6da 55%, #b8c7c8 100%); }
  .step-balloons { height: 168px; background: linear-gradient(180deg, #b7d3ec 0%, #cfe1f1 60%, #e0746a 100%); }

  .author {
    position: absolute; left: 426px; top: 46px;
    font-family: "Josefin Sans", sans-serif;
    font-size: 40px; line-height: 1; letter-spacing: 9px; color: var(--navy);
    white-space: nowrap;
  }
  .author-first { font-weight: 300; }
  .author-last { font-weight: 600; }

  .title { font-family: "Marcellus", serif; font-weight: 400; color: var(--navy); }
  .title span { position: absolute; left: 408px; line-height: 1; white-space: nowrap; }
  .title-article { top: 830px; font-size: 61px; }
  .title-gold { top: 902px; font-size: 58px; color: var(--gold); letter-spacing: 8px; }
  .title-big { font-size: 84px; letter-spacing: 1px; }
  .title-line-one { top: 977px; }
  .title-line-two { top: 1087px; }
</style>
</head>
<body>
<main class="cover">
  <section class="step-strip">
    <div class="step-photo step-toys" role="img" aria-label="Photo of colourful wooden stacking toys on a shelf"></div>
    <div class="step-photo step-tools" role="img" aria-label="Photo of a cordless drill, wrenches and work gloves laid on concrete"></div>
    <div class="step-photo step-sand" role="img" aria-label="Photo of the word forgiveness written in sand with a small heart"></div>
    <div class="step-photo step-mic" role="img" aria-label="Photo of a studio microphone on a stand in a bright room"></div>
    <div class="step-photo step-thanks" role="img" aria-label="Photo of autumn pumpkin decorations spelling give thanks"></div>
    <div class="step-photo step-calm" role="img" aria-label="Photo of a woman meditating outdoors against misty hills"></div>
    <div class="step-photo step-balloons" role="img" aria-label="Photo of many hot air balloons rising into a blue sky"></div>
  </section>

  <p class="author"><span class="author-first">MAREN</span><span class="author-last">ELLIS</span></p>

  <h1 class="title">
    <span class="title-article">The</span>
    <span class="title-gold">MORNING</span>
    <span class="title-big title-line-one">LANTERN</span>
    <span class="title-big title-line-two">METHOD</span>
  </h1>
</main>
</body>
</html>
```